2-Sided Law Firm Business Card

This is the second phase of a law firm "rebrand project" in which I'm changing my firm's name to "Brockwyn Law PLLC." The first phase was a logo contest -- I will be updating this project sometime tomorrow with the winning logo design.

The business card will need to include, on its reverse side, the firm's logo and tag line, "Legal Counsel for the Innovative Company," on a darker background whose color is consistent with the logo design.

The face of the card will need to include the firm's name (logo), website url, and phone number. It will also need to include, at the very least, the name of the attorney, the attorney's title, the attorney's email address, and the attorney's twitter feed. (I do not maintain a dedicated office and therefore the card does not need to specify a business address.) I will provide the actual contact information to the winning designer. Until then, you may use fictional data in suggesting your proposed design.

My firm specializes in representing startup companies. This means I routinely interact with young entrepreneurs and the (typically) older, more experienced investors who fund them. I need to appeal to the former without offending the latter. I'm interesting in conveying the idea that my firm is a credible alternative to larger, brand-name firms. I use these words in positioning my firm in this market: creative; flexible; fair; practical; experienced. The winning design needs to convey this idea.

I'm will also be re-working my website soon and will likely use noto sans and noto serif as my primary website fonts. I'd like the business card to use a font that is similar, but also compatible with the font used in the firm's logo.

Target Market(s)

Young entrepreneurs and older investors who collaborate in the formation and funding of high-tech startup companies located in the Pacific Northwest.

Industry/Entity Type

Law Firm

Font styles to use
Serif
Sans Serif

Requirements
Must have
• Firm logo, firm tag line, firm website url, firm phone number, attorney name, attorney title, attorney email address, and attorney twitter.

The attached pdf indicates kind of what I have in mind, recognizing that it is my amateur attempt at doing what I'm hoping the winning designer is able to do so much better.
Nice to have
• Adding a statement about my practice areas, if there's room, might be nice:

"General Counsel | Business Formation | Intellectual Property | Angel Investments & Venture Capital | Mergers & Acquisitions"

Also, I make it a point to meet with clients "by appointment only" in the following areas of Seattle: "Freemont | Pioneer Square | Redmond | South Lake Union." It might be worth including as well, but only if the card itself isn't too cramped. I favor "too simple" over "too informative."
Should not have
• Do NOT put the scales of justice anywhere on this business card. I am a business lawyer.

```html
<!DOCTYPE html>
<html lang="en">
<head>
<meta charset="utf-8">
<title>Brockwyn Law PLLC – Business Card</title>
<link rel="stylesheet" href="https://fonts.googleapis.com/css2?family=Noto+Sans:wght@400&display=swap">
<style>
  :root {
    --page: #ffffff;
    --card-navy: #151a38;
    --text-white: #ffffff;
    --wordmark-grey: #6b6b6b;
    --service-grey: #7a7a7a;
    --footer-grey: #8a8a8a;
    --placeholder-grey: #686868;
  }
  * { margin: 0; padding: 0; box-sizing: border-box; }
  html, body {
    width: 1131px;
    height: 1200px;
    overflow: hidden;
    background: var(--page);
    font-family: "Noto Sans", Tahoma, sans-serif;
  }
  .sheet {
    position: relative;
    width: 1131px;
    height: 1200px;
  }
  .card {
    position: absolute;
    left: 49px;
    width: 1038px;
    background: var(--card-navy);
  }
  .card--front { top: 0; height: 592px; }
  .card--back { top: 605px; height: 590px; }

  .attorney {
    position: absolute;
    right: 9px;
    top: 2px;
    text-align: right;
    color: var(--text-white);
  }
  .attorney__name { font-size: 35px; line-height: 1.15; }
  .attorney__title { font-size: 20px; line-height: 1.2; }
  .attorney__contact {
    margin-top: 36px;
    font-size: 20px;
    line-height: 29px;
  }

  .firm-mark {
    position: absolute;
    left: 352px;
    top: 222px;
    color: var(--wordmark-grey);
  }
  .firm-mark__name {
    font-size: 100px;
    line-height: 1;
    letter-spacing: -1px;
  }
  .firm-mark__suffix {
    position: absolute;
    right: -64px;
    top: 104px;
    font-size: 22px;
    white-space: nowrap;
  }

  .services {
    position: absolute;
    left: 7px;
    bottom: 6px;
    list-style: none;
    color: var(--service-grey);
    font-size: 24px;
    line-height: 29px;
  }

  .firm-contact {
    position: absolute;
    right: 7px;
    bottom: 10px;
    color: var(--footer-grey);
    font-size: 21px;
  }

  .back-placeholder {
    position: absolute;
    left: 442px;
    top: 233px;
    color: var(--placeholder-grey);
    font-size: 44px;
    line-height: 64px;
  }
</style>
</head>
<body>
<main class="sheet">
  <section class="card card--front" aria-label="Card front">
    <div class="attorney">
      <p class="attorney__name">Dana K. Brockwyn</p>
      <p class="attorney__title">Startup Attorney</p>
      <p class="attorney__contact">dana@brockwynlawpllc.com<br>@danabrockwyn</p>
    </div>

    <div class="firm-mark">
      <p class="firm-mark__name">Brockwyn</p>
      <p class="firm-mark__suffix">Law PLLC</p>
    </div>

    <ul class="services">
      <li>General Counsel</li>
      <li>Business Formation</li>
      <li>Intellectual Property</li>
      <li>Angel Investments</li>
      <li>Venture Capital</li>
      <li>Mergers &amp; Acquisitions</li>
    </ul>

    <p class="firm-contact">www.brockwynlawpllc.com| 425.555.0147</p>
  </section>

  <section class="card card--back" aria-label="Card back">
    <p class="back-placeholder">Logo &amp;<br>Tag line</p>
  </section>
</main>
</body>
</html>
```